Web Design For Staffing Company

We need a homepage web design for a technical staffing company.

Please see attached brief for project details.

please make the site modern with bold colors while matching the logo

Be sure to read the attached breif in full beforehand.

Target Market(s)

technical companies looking to hire talent

Industry/Entity Type

Staffing

Number of Pages Required

1 page

Font styles to use
Sans Serif

```html
<!DOCTYPE html>
<html lang="en">
<head>
<meta charset="utf-8">
<title>Veritane Staffing – Home</title>
<link href="https://fonts.googleapis.com/css2?family=Fira+Sans:wght@300;400;500;600&display=swap" rel="stylesheet">
<style>
:root{
  --page-bg:#dededc;
  --white:#ffffff;
  --navy:#163d5e;
  --navy-deep:#123452;
  --blue:#2d7bbf;
  --blue-bright:#3b91d6;
  --accent-text:#2f8ad2;
  --band-grey:#ececec;
  --ink:#2a3a4a;
  --muted:#8a97a3;
}
*{box-sizing:border-box;margin:0;padding:0}
html,body{width:736px;height:1200px;overflow:hidden}
body{background:var(--page-bg);font-family:"Fira Sans",Arial,sans-serif;color:var(--ink);position:relative}
.site{position:absolute;left:79px;top:59px;width:578px;height:1080px;background:var(--white);border-radius:18px;overflow:hidden}
.abs{position:absolute}

/* header */
.brand{left:73px;top:14px;display:flex;align-items:center;gap:5px;font-weight:600;font-size:14px;color:var(--navy)}
.brand-dot{width:10px;height:10px;border-radius:50%;background:var(--blue-bright)}
.nav{right:72px;top:20px;display:flex;gap:12px;font-size:7px;letter-spacing:.2px;color:var(--ink)}

/* hero */
.hero{left:0;top:51px;width:578px;height:222px;background:linear-gradient(180deg,#2c78b9 0%,#2e7ec0 45%,#2a6fae 100%)}
.hero-title{left:0;top:120px;width:578px;text-align:center;color:#fff;font-weight:300;font-size:16px;line-height:22px}
.hero-rule{left:241px;top:225px;width:96px;height:1px;background:rgba(255,255,255,.7)}
.btn-outline{display:flex;align-items:center;justify-content:center;border:1px solid #fff;border-radius:3px;color:#fff}
.hero-btn{top:243px;width:101px;height:24px;font-size:11.5px;letter-spacing:.4px}

/* search */
.search-band{left:0;top:273px;width:578px;height:66px;background:var(--band-grey)}
.field{top:294px;height:24px;width:158px;background:#fff;border:1px solid #8fbde3;border-radius:2px;display:flex;align-items:center;gap:6px;padding-left:9px;font-size:10px;color:#b5bcc3;font-weight:300}
.search-btn{left:408px;top:294px;width:92px;height:24px;background:var(--navy);color:#fff;font-size:10px;font-weight:600;display:flex;align-items:center;justify-content:center}

/* about */
.about-title{left:0;top:360px;width:578px;text-align:center;font-size:15px;font-weight:300;color:var(--accent-text)}
.about-rule{left:239px;top:381px;width:100px;height:1px;background:var(--accent-text)}
.about-text{left:60px;top:390px;width:458px;text-align:center;font-size:7px;line-height:11.3px;color:var(--navy)}

/* split */
.split-left{left:0;top:435px;width:289px;height:178px;background:linear-gradient(180deg,#16406a 0%,#143a5c 60%,#112f4b 100%)}
.split-right{left:289px;top:435px;width:289px;height:178px;background:linear-gradient(180deg,#2e7dc0 0%,#2b75b7 100%)}
.split-copy{top:474px;width:170px;font-size:6.5px;line-height:10.7px;color:#fff}
.split-btn{top:556px;width:71px;height:17px;font-size:8px;border-radius:2px}
.btn-muted{border-color:#3b91d6;color:#3b91d6}

/* testimonials */
.testi-band{left:0;top:613px;width:578px;height:225px;background:var(--band-grey)}
.testi-title{left:0;top:642px;width:578px;text-align:center;font-size:15px;font-weight:300;color:var(--navy)}
.testi-card{top:678px;width:211px;height:123px;background:#fff;text-align:center}
.quote{position:absolute;left:0;top:12px;width:100%;font-size:12px;font-weight:600;color:var(--blue-bright);line-height:10px}
.testi-text{position:absolute;left:14px;top:31px;width:183px;font-size:4.4px;line-height:7.2px;color:#333}
.testi-rule{position:absolute;left:75px;top:63px;width:61px;height:1px;background:#b6d4ee}
.avatar{position:absolute;left:92px;top:70px;width:28px;height:28px;border-radius:50%;border:1px solid #333;background:radial-gradient(circle at 50% 40%,#e5a24a 0%,#6c6a78 55%,#2b3a4d 100%)}
.testi-name{position:absolute;left:0;top:102px;width:100%;font-size:5.5px;color:var(--navy)}
.testi-role{position:absolute;left:0;top:111px;width:100%;font-size:3.8px;color:#666}

/* cta */
.cta{top:860px;width:211px;height:92px;border-radius:6px;text-align:center;color:#fff}
.cta-blue{left:73px;background:linear-gradient(180deg,#3484c7 0%,#2e7cc0 100%)}
.cta-navy{left:294px;background:linear-gradient(180deg,#163d5e 0%,#133755 100%)}
.cta-title{position:absolute;left:0;top:12px;width:100%;font-size:13.5px;font-weight:300;line-height:19.5px}
.cta-btn{position:absolute;left:19px;top:60px;width:172px;height:17px;font-size:8.5px;font-weight:300;border-radius:3px}

/* footer */
.footer{left:0;top:975px;width:578px;height:105px;background:var(--navy)}
.foot-col{top:990px;width:127px;color:#fff}
.foot-head{font-size:11px;color:var(--blue-bright);margin-bottom:6px}
.foot-text{font-size:6.6px;line-height:10px;height:32px}
.foot-btn{position:absolute;left:0;top:56px;width:127px;height:17px;background:var(--blue-bright);border-radius:2px;font-size:8.5px;font-weight:300;display:flex;align-items:center;justify-content:center}
</style>
</head>
<body>
<div class="site">

  <header>
    <div class="abs brand"><span class="brand-dot"></span>Veritane Staffing</div>
    <nav class="abs nav"><span>HOME</span><span>ABOUT</span><span>JOB SEEKERS</span><span>CLIENTS</span><span>CONTACT</span></nav>
  </header>

  <section>
    <div class="abs hero" role="img" aria-label="Blue-toned photograph of a suspension bridge at dusk"></div>
    <h1 class="abs hero-title">The Right People For The Right Jobs!<br>Bridging the talent gap in Technical Staffing</h1>
    <div class="abs hero-rule"></div>
    <div class="abs btn-outline hero-btn" style="left:182px">HIRE TALENT</div>
    <div class="abs btn-outline hero-btn" style="left:295px">GET HIRED</div>
  </section>

  <section>
    <div class="abs search-band"></div>
    <div class="abs field" style="left:78px">
      <svg width="13" height="13" viewBox="0 0 13 13"><circle cx="4" cy="9" r="3" fill="#c5c9ce"/><path d="M6 7 L11 2 M9 4 L11 6" stroke="#c5c9ce" stroke-width="1.6" fill="none"/></svg>
      Keywords
    </div>
    <div class="abs field" style="left:245px">
      <svg width="10" height="13" viewBox="0 0 10 13"><path d="M5 12 C1 7 1 6 1 5 a4 4 0 0 1 8 0 c0 1 0 2 -4 7z" fill="#c5c9ce"/><circle cx="5" cy="5" r="1.6" fill="#fff"/></svg>
      Location
    </div>
    <div class="abs search-btn">SEARCH JOBS</div>
  </section>

  <section>
    <h2 class="abs about-title">About us</h2>
    <div class="abs about-rule"></div>
    <p class="abs about-text">Veritane Staffing is a National Technical Staffing and Recruiting Solutions Provider founded in 2013 focused on matching contract and full time Engineering and IT professionals with new and exciting employment opportunities!</p>
  </section>

  <section>
    <div class="abs split-left" role="img" aria-label="Dark navy photograph of a cable-stayed bridge"></div>
    <div class="abs split-right" role="img" aria-label="Blue-toned photograph of a bridge over the bay"></div>
    <p class="abs split-copy" style="left:73px">WE LOVE TO RECRUIT! It's our passion and we take it very seriously! It is not easy for JOB SEEKERS to put their job search efforts and trust in the hands of someone else, especially when there are so many Staffing Firms to choose from. So how do you know you are choosing the best Staffing Representation possible?</p>
    <p class="abs split-copy" style="left:326px">Are you responsible for Technical Staffing within your organization? Are you satisfied with your current Supplier(s)' overall performance? Does it appear they identify potential Candidate(s) based purely on "buzz-word" searches? Is it evident they just do not grasp the scope and responsibilities of your technical staffing need(s)?</p>
    <div class="abs btn-outline btn-muted split-btn" style="left:73px">Learn More</div>
    <div class="abs btn-outline btn-muted split-btn" style="left:152px">View Jobs</div>
    <div class="abs btn-outline split-btn" style="left:325px">Learn More</div>
    <div class="abs btn-outline split-btn" style="left:404px">Hire Talent</div>
  </section>

  <section>
    <div class="abs testi-band"></div>
    <h2 class="abs testi-title">Client Testimonials</h2>
    <article class="abs testi-card" style="left:73px">
      <span class="quote">&ldquo;</span>
      <p class="testi-text">Dana Whitlow is an excellent recruiter. She is articulate, honest, has a good nature and is an effective information conduit between her clients and candidates. She gave me the feeling she is there for the big picture desiring to forge a future relationship that will be mutually beneficial to both of us.</p>
      <div class="testi-rule"></div>
      <div class="avatar" role="img" aria-label="Round profile photo of a bridge at sunset"></div>
      <p class="testi-name">Sam R.</p>
      <p class="testi-role">Electrical Test Engineer in the Automotive Sector</p>
    </article>
    <article class="abs testi-card" style="left:294px">
      <span class="quote">&ldquo;</span>
      <p class="testi-text">Dana Whitlow is an excellent recruiter. She is articulate, honest, has a good nature and is an effective information conduit between her clients and candidates. She gave me the feeling she is there for the big picture desiring to forge a future relationship that will be mutually beneficial to both of us.</p>
      <div class="testi-rule"></div>
      <div class="avatar" role="img" aria-label="Round profile photo of a bridge at sunset"></div>
      <p class="testi-name">Sam R.</p>
      <p class="testi-role">Electrical Test Engineer in the Automotive Sector</p>
    </article>
  </section>

  <section>
    <div class="abs cta cta-blue" role="img" aria-label="Blue-toned bridge photograph behind call to action">
      <h3 class="cta-title">Looking for Career<br>Opportunities</h3>
      <div class="btn-outline cta-btn">Search Jobs</div>
    </div>
    <div class="abs cta cta-navy" role="img" aria-label="Navy-toned bridge photograph behind call to action">
      <h3 class="cta-title">Looking for Career-Minded<br>Candidates?</h3>
      <div class="btn-outline btn-muted cta-btn">Request Talent</div>
    </div>
  </section>

  <footer>
    <div class="abs footer"></div>
    <div class="abs foot-col" style="left:73px">
      <h4 class="foot-head">Get Hired</h4>
      <p class="foot-text">Search our extensive list of available jobs to find your ideal match.</p>
      <div class="foot-btn">Search Jobs</div>
    </div>
    <div class="abs foot-col" style="left:226px">
      <h4 class="foot-head">Hire Talent</h4>
      <p class="foot-text">We're here to provide the people you need to get work done.</p>
      <div class="foot-btn">Search Jobs</div>
    </div>
    <div class="abs foot-col" style="left:379px">
      <h4 class="foot-head">Get in Touch</h4>
      <p class="foot-text">Veritane Staffing, Inc.<br>48 Harbor Lane, Suite 2, 3rd floor<br>Millbrook, MA 01900</p>
      <div class="foot-btn">Contact Us</div>
    </div>
  </footer>

</div>
</body>
</html>
```